Coffee and fruit juice

We are a malaysian restaurant that also serves aussie coffee and breakfast from 7am to 11am. After 11am we serve malaysian food but we also have a salad and sandwhich bar for people to choose from. We need a poster to hang outside our door to let people know that we are now also serving aussie coffee and breakfast as well as our usual malaysian cuisine.

Target Market(s)

Office location

Industry/Entity Type

Restaurant

Font styles to use
Decorative
Script

Requirements
Must have
• images and word
Nice to have
• something bold to attract people's attention

```html
<!DOCTYPE html>
<html lang="en">
<head>
<meta charset="UTF-8">
<title>Rempah Desa – Breakfast and Coffee</title>
<link rel="stylesheet" href="https://fonts.googleapis.com/css2?family=Playfair+Display:ital,wght@1,400&family=Parisienne&family=Abril+Fatface&family=Archivo+Black&family=Comfortaa:wght@700&display=swap">
<style>
  :root {
    --wood-dark: #2a160c;
    --wood-mid: #4a2b1a;
    --wood-light: #5e3822;
    --ink-white: #ffffff;
    --accent-green: #17f08e;
    --juice: #f0a016;
    --toast: #d29a5c;
    --cup: #ece6dc;
    --salad: #5f9a2a;
  }
  * { margin: 0; padding: 0; box-sizing: border-box; }
  html, body { width: 849px; height: 1200px; overflow: hidden; }
  body { background: var(--wood-dark); }
  .poster {
    position: relative;
    width: 849px;
    height: 1200px;
    overflow: hidden;
    background:
      radial-gradient(ellipse at 55% 40%, rgba(120,72,42,0.55), rgba(0,0,0,0) 65%),
      linear-gradient(180deg, var(--wood-mid) 0%, var(--wood-light) 35%, var(--wood-mid) 70%, var(--wood-dark) 100%);
  }
  .plank-seam {
    position: absolute; left: 0; width: 849px; height: 2px;
    background: rgba(20,10,4,0.45);
  }
  .brand-name {
    position: absolute; left: 20px; top: 46px;
    font-family: "Playfair Display", serif; font-style: italic;
    font-size: 36px; letter-spacing: 8px; line-height: 1; color: var(--ink-white);
  }
  .headline {
    position: absolute; left: 0; top: 104px; width: 849px;
    text-align: center; font-weight: 400;
    font-family: "Parisienne", cursive;
    font-size: 88px; line-height: 56px; color: var(--ink-white);
  }
  .breakfast-photo {
    position: absolute; left: 66px; top: 276px; width: 726px; height: 476px;
    border-radius: 36px;
    background:
      linear-gradient(180deg, rgba(255,255,255,0) 55%, rgba(236,230,220,0.55) 80%, rgba(236,230,220,0) 100%),
      linear-gradient(90deg, var(--juice) 0%, var(--juice) 20%, var(--toast) 38%, var(--cup) 52%, var(--toast) 66%, var(--salad) 84%, var(--salad) 100%);
  }
  .hours {
    position: absolute; left: 0; top: 770px; width: 849px; height: 190px;
    color: var(--accent-green);
  }
  .hours-seven {
    position: absolute; left: 190px; top: -14px;
    font-family: "Abril Fatface", serif; font-size: 220px; line-height: 1;
    transform: scaleX(1.35); transform-origin: left top;
  }
  .hours-end {
    position: absolute; left: 352px; top: -12px;
    font-family: "Archivo Black", sans-serif; font-size: 215px; line-height: 1;
    letter-spacing: -6px;
    transform: scaleX(0.9); transform-origin: left top;
  }
  .am {
    position: absolute;
    font-family: "Comfortaa", sans-serif; font-size: 30px; font-weight: 700;
    line-height: 1; color: var(--accent-green);
  }
  .am-start { left: 292px; top: 905px; transform: rotate(-90deg); transform-origin: left top; }
  .am-end { left: 688px; top: 872px; transform: rotate(90deg); transform-origin: left top; }
  .later-menu {
    position: absolute; left: 0; top: 998px; width: 849px;
    text-align: center;
    font-family: "Comfortaa", sans-serif; font-weight: 700;
    font-size: 38px; line-height: 44px; letter-spacing: 1.5px; color: var(--accent-green);
  }
  .footer-rule {
    position: absolute; left: 150px; top: 1107px; width: 547px; height: 2px;
    background: var(--ink-white);
  }
</style>
</head>
<body>
  <main class="poster">
    <div class="plank-seam" style="top:78px"></div>
    <div class="plank-seam" style="top:258px"></div>
    <div class="plank-seam" style="top:790px"></div>
    <div class="plank-seam" style="top:965px"></div>

    <p class="brand-name">REMPAH DESA</p>

    <h1 class="headline">Breakfast and coffee<br>available</h1>

    <div class="breakfast-photo" role="img" aria-label="Glass of orange juice, toasted bacon and cheese sandwiches, a cup of coffee on a saucer and a bowl of green salad"></div>

    <div class="hours" aria-label="7am to 11am">
      <span class="hours-seven">7</span>
      <span class="hours-end">-11</span>
    </div>
    <span class="am am-start">am</span>
    <span class="am am-end">am</span>

    <p class="later-menu">Malaysia foods,Salad Buns and<br>ECT available from 10:30am</p>

    <div class="footer-rule"></div>
  </main>
</body>
</html>
```